Visitenkarten-Design für italienisches Küchenschiff
Zielgruppe
Restaurantschiff Morvella
Aufgabenstellung
Wir sind ein italienische Küche Schiff auf der Binnenalster in Hamburg und wollen den schönen Blick und gerne auch die italienischen Farben widerspiegeln...ich brauche das einmal neutral für den normalen Gast....und würde das denn..wenn es denn gut wird...auch gerne individell mit m e i n e r Tel Nr und auch für meine führenden Mitarbeiter personalisieren...aber...zuerst natürlich das neutrale...dazu schicke ich die alte Karte mit dem auch alten Logo was nicht unbedingt verwendet werden muss...

```html
<!DOCTYPE html>
<html lang="de">
<head>
<meta charset="utf-8">
<title>Morvella – Visitenkarte</title>
<link href="https://fonts.googleapis.com/css2?family=Advent+Pro:wght@300&display=swap" rel="stylesheet">
<style>
  :root {
    --stage: #4d4d4d;
    --card: #464342;
    --ink: #a3968a;
    --ink-soft: #9a8d80;
    --rule: #504c4a;
    --green: #009a57;
    --white: #ffffff;
    --red: #a7282f;
  }
  html, body {
    margin: 0;
    width: 1200px;
    height: 1200px;
    overflow: hidden;
    background: var(--stage);
    font-family: "Advent Pro", sans-serif;
    font-weight: 300;
  }
  .canvas { position: relative; width: 1200px; height: 1200px; }
  .card {
    position: absolute;
    top: 437px;
    width: 510px;
    height: 327px;
    background: var(--card);
    color: var(--ink);
    overflow: hidden;
  }
  .card--front { left: 61px; }
  .card--back { left: 628px; }
  .card p { margin: 0; position: absolute; white-space: nowrap; line-height: 1; }

  .brand-name {
    left: 25px; top: 618px; font-size: 40px; letter-spacing: 1px;
  }
  .divider {
    position: absolute; left: 251px; top: 60px;
    width: 1px; height: 242px; background: var(--rule);
  }
  .info { font-size: 16.5px; left: 269px; }
  .heading { font-size: 21px; }

  .photo {
    position: absolute; left: 23px; width: 211px; height: 128px;
  }
  .photo--dining {
    top: 19px;
    background: linear-gradient(180deg, #c9b9a2 0%, #6f8aa8 22%, #8ea9c4 45%, #7a5a3e 58%, #a23232 72%, #e6e3df 100%);
  }
  .photo--skyline {
    top: 162px;
    background: linear-gradient(180deg, #4c3d4f 0%, #6d5b70 35%, #5a4d5a 55%, #a6998a 66%, #2c2a38 80%, #1d1d28 100%);
  }
  .back-text { left: 258px; }
  .right { text-align: right; }
  .flag {
    position: absolute; left: 0; top: 300px; width: 510px; height: 9px; display: flex;
  }
  .flag span { flex: 1; }
  .flag .green { background: var(--green); }
  .flag .white { background: var(--white); }
  .flag .red { background: var(--red); }
</style>
</head>
<body>
<div class="canvas">
  <section class="card card--front">
    <p class="brand-name" style="top:180px">MORVELLA</p>
    <div class="divider"></div>
    <p class="info" style="top:62px">Schiffsrestaurant Morvella</p>
    <p class="info" style="top:86px">Uferkai (Wasserseite)</p>
    <p class="info" style="top:109px">20097 Hamburg</p>
    <p class="info heading" style="top:143px">Kontakt</p>
    <p class="info" style="top:172px">Tel: +49 040 / 55 18 46</p>
    <p class="info" style="top:195px">Fax:&nbsp;&nbsp;&nbsp;+49 040 / 55 18 4</p>
    <p class="info" style="top:219px">www.seeschiff-morvella.de</p>
    <p class="info" style="top:242px">E-Mail: info(at)seeschiff-morvella.de</p>
  </section>

  <section class="card card--back">
    <div class="photo photo--dining" role="img" aria-label="Gedeckter Tisch im Schiffsrestaurant mit Blick auf die Binnenalster"></div>
    <div class="photo photo--skyline" role="img" aria-label="Beleuchtete Uferpromenade der Binnenalster bei Nacht"></div>

    <p class="info back-text heading" style="top:62px">Öffnungszeiten</p>
    <p class="info back-text" style="top:87px">Montag - Sonntag</p>
    <p class="info right" style="top:87px; right:42px">12:00 - 23:00</p>
    <p class="info right" style="top:108px; right:42px">Küche bis 22:00</p>
    <p class="info back-text" style="top:129px">Sonntags haben wir derzeit geöffnet.</p>

    <p class="info back-text heading" style="top:176px">Reservierungen</p>
    <p class="info back-text" style="top:200px">Wollen Sie einen Tisch reservieren? Wir</p>
    <p class="info back-text" style="top:221px">freuen uns auf Ihren Anruf oder eine:</p>
    <p class="info back-text" style="top:242px">reservierung(at)seeschiff-morvella.de</p>

    <div class="flag"><span class="green"></span><span class="white"></span><span class="red"></span></div>
  </section>
</div>
</body>
</html>
```